Employee Portal UI Design - Modern and Clean

We are an agency tasked with developing a team portal for a company that has many employees. As we embark on this project, we seek a great UI design to accompany the requirements our client has for this project. We already have several screens mocked up that can be used as reference for the overall idea. Currently, we are only looking for the main dashboard's home page, user registration screen, and account settings page to be designed. The main brand colors are red but other accents can be used as well. The client's vision is for modern & minimalist to be at the center. We have a specific font to be used, but if you don't have access to it, you can just use a similar font.Main color: #DD0031The sub menus (do not need to be designed) would be:>Performance Reviews>Posts>Team directory>Calendar>Tasks>Documents>LinksWe would prefer the design be made in Adobe XD.

Industry/Entity Type

Fast Food Restaurant

Number of Pages Required

1 page

Font styles to use
Sans Serif

Colors
ec1f27

Requirements
Must have
• Color: #DD0031 (highlights)

```html
<!DOCTYPE html>
<html lang="en">
<head>
<meta charset="utf-8">
<title>My Profile – Settings</title>
<link rel="stylesheet" href="https://fonts.googleapis.com/css2?family=Open+Sans:wght@300;400;600;700&display=swap">
<style>
  :root {
    --brand: #cf0036;
    --brand-soft: #e58a9f;
    --band: #cccccc;
    --page: #ffffff;
    --card: #ffffff;
    --line: #c4c4c4;
    --field-line: #dcdcdc;
    --ink: #333333;
    --muted: #8e8e8e;
    --icon: #9a9a9a;
    --avatar: #999999;
  }
  * { box-sizing: border-box; margin: 0; padding: 0; }
  html, body { width: 1200px; height: 1000px; overflow: hidden; background: var(--page); }
  body { font-family: "Open Sans", sans-serif; color: var(--ink); position: relative; }

  .settings-band { position: absolute; left: 0; top: 125px; width: 1200px; height: 750px; background: var(--band); }

  .section-title { position: absolute; top: 144px; font-weight: 300; font-size: 34px; line-height: 46px; color: var(--ink); text-align: center; }
  .section-title--settings { left: 30px; width: 250px; }
  .section-title--profile { left: 310px; width: 860px; }

  .settings-nav { position: absolute; left: 30px; top: 190px; width: 250px; background: var(--card); border: 1px solid var(--line); border-radius: 3px; list-style: none; overflow: hidden; }
  .settings-nav li { height: 31px; line-height: 30px; padding-left: 9px; font-size: 15px; border-top: 1px solid var(--line); position: relative; }
  .settings-nav li:first-child { border-top: none; }
  .settings-nav .is-active { color: var(--brand); }
  .settings-nav .is-active::after { content: ""; position: absolute; right: 0; top: 0; width: 10px; height: 100%; background: var(--brand); }

  .profile-card { position: absolute; left: 310px; top: 190px; width: 860px; height: 656px; background: var(--card); border: 1px solid var(--line); border-radius: 3px; }

  .avatar { position: absolute; left: 91px; top: 29px; width: 130px; height: 130px; }
  .profile-name { position: absolute; left: 56px; top: 161px; width: 200px; text-align: center; font-weight: 700; font-size: 21px; color: #666; }

  .profile-form { position: absolute; left: 0; top: 0; }
  .field { position: absolute; left: 250px; width: 580px; height: 42px; }
  .field label { position: absolute; left: 0; width: 160px; top: 0; line-height: 42px; text-align: right; font-size: 15px; color: var(--ink); }
  .field .input { position: absolute; left: 180px; top: 0; width: 400px; height: 42px; border: 1px solid var(--field-line); border-radius: 2px; padding-left: 13px; line-height: 40px; font-size: 15px; color: var(--muted); }
  .field .input svg { position: absolute; right: 13px; top: 13px; width: 14px; height: 14px; fill: var(--icon); }
  .field--password label { color: var(--brand); }
  .field--password .input svg { fill: var(--brand-soft); }

  .save-button { position: absolute; left: 630px; top: 575px; width: 200px; height: 50px; background: var(--brand); color: #fff; border: none; border-radius: 2px; font-family: "Open Sans", sans-serif; font-size: 22px; font-weight: 400; }
</style>
</head>
<body>
  <div class="settings-band"></div>

  <h2 class="section-title section-title--settings">Settings</h2>
  <ul class="settings-nav">
    <li class="is-active">My Profile</li>
    <li>Notifications</li>
    <li>User Roles</li>
    <li>Role Permissions</li>
    <li>Custom Links</li>
    <li>Plans &amp; Billing</li>
  </ul>

  <h1 class="section-title section-title--profile">My Profile</h1>

  <section class="profile-card">
    <svg class="avatar" viewBox="0 0 130 130" aria-hidden="true">
      <circle cx="65" cy="65" r="64" fill="var(--avatar)" stroke="#d6d6d6" stroke-width="2"/>
      <path d="M65 20c-13 0-21 9-21 22 0 11 5 20 11 25v6c-12 4-24 9-27 14-2 4-2 10-1 15 10 5 25 8 38 8s28-3 38-8c1-5 1-11-1-15-3-5-15-10-27-14v-6c6-5 11-14 11-25 0-13-8-22-21-22z" fill="none" stroke="#fff" stroke-width="5" stroke-linejoin="round"/>
      <circle cx="117" cy="117" r="12" fill="var(--brand)"/>
      <path d="M111 123l1.5-4.5 7-7 3 3-7 7z" fill="#fff"/>
    </svg>
    <div class="profile-name">Daniel Reyes</div>

    <form class="profile-form">
      <div class="field" style="top:29px"><label>First Name</label><div class="input">Daniel<svg viewBox="0 0 14 14"><circle cx="7" cy="4" r="3"/><path d="M1.5 14c0-4 2.5-6 5.5-6s5.5 2 5.5 6z"/></svg></div></div>
      <div class="field" style="top:89px"><label>Last Name</label><div class="input">Reyes<svg viewBox="0 0 14 14"><circle cx="7" cy="4" r="3"/><path d="M1.5 14c0-4 2.5-6 5.5-6s5.5 2 5.5 6z"/></svg></div></div>
      <div class="field" style="top:149px"><label>Email</label><div class="input">dan.reyes@mailbox.test<svg viewBox="0 0 14 14"><path d="M0 2.5h14v1L7 8 0 3.5z"/><path d="M0 5l7 4.5L14 5v7H0z"/></svg></div></div>
      <div class="field" style="top:209px"><label>Phone</label><div class="input">555-204-7781<svg viewBox="0 0 14 14"><path d="M3 0.5l2.5 3-1.5 2c1 2 2.5 3.5 4.5 4.5l2-1.5 3 2.5-1.5 2.5C7 13.5 0.5 7 1 1.5z"/></svg></div></div>
      <div class="field" style="top:269px"><label>Address</label><div class="input">418 Harbor Way<svg viewBox="0 0 14 14"><path d="M7 0a5 5 0 0 0-5 5c0 4 5 9 5 9s5-5 5-9a5 5 0 0 0-5-5zm0 7a2 2 0 1 1 0-4 2 2 0 0 1 0 4z"/></svg></div></div>
      <div class="field" style="top:329px"><label>City</label><div class="input">Lakeview<svg viewBox="0 0 14 14"><path d="M7 0a5 5 0 0 0-5 5c0 4 5 9 5 9s5-5 5-9a5 5 0 0 0-5-5zm0 7a2 2 0 1 1 0-4 2 2 0 0 1 0 4z"/></svg></div></div>
      <div class="field" style="top:389px"><label>State</label><div class="input">Florida<svg viewBox="0 0 14 14"><path d="M7 0a5 5 0 0 0-5 5c0 4 5 9 5 9s5-5 5-9a5 5 0 0 0-5-5zm0 7a2 2 0 1 1 0-4 2 2 0 0 1 0 4z"/></svg></div></div>
      <div class="field" style="top:449px"><label>Zip Code</label><div class="input">33470<svg viewBox="0 0 14 14"><path d="M7 0a5 5 0 0 0-5 5c0 4 5 9 5 9s5-5 5-9a5 5 0 0 0-5-5zm0 7a2 2 0 1 1 0-4 2 2 0 0 1 0 4z"/></svg></div></div>
      <div class="field field--password" style="top:509px"><label>New Password</label><div class="input"><svg viewBox="0 0 14 14"><path d="M4 6V4.5a3 3 0 0 1 6 0V6h-1.5V4.5a1.5 1.5 0 0 0-3 0V6z"/><rect x="2" y="6" width="10" height="8" rx="1"/></svg></div></div>
      <button class="save-button" type="button">Save Changes</button>
    </form>
  </section>
</body>
</html>
```